English and Spanish Language School Needs a Business Card

Need a business card design a startup company called Corvella Language School. The company will offer English and Spanish conversational level courses designed to make the learner feel comfortable with grammar and vocabulary. We would like to see a logo with some colour that should communicate learning, growth.

Target Market(s)

Consumers and businesses

Industry/Entity Type

Education

Contact Information for Business Card

TBD

Font styles to use
Serif

Requirements
Must have
• Include the following
• Logo
• Name
• Title
• Cellphone Number
• Office Phone number
• Email address
• Office Address

```html
<!DOCTYPE html>
<html lang="en">
<head>
<meta charset="utf-8">
<title>Corvella Language School – Business Card</title>
<link rel="stylesheet" href="https://fonts.googleapis.com/css2?family=Tinos:wght@400;700&display=swap">
<style>
  :root {
    --backdrop: #3a3a3c;
    --card: #1f2124;
    --red: #c8202a;
    --teal: #12a0ad;
    --card-w: 900px;
    --card-h: 514px;
  }
  * { box-sizing: border-box; margin: 0; padding: 0; }
  html, body {
    width: 1200px;
    height: 1189px;
    overflow: hidden;
    background: var(--backdrop);
    font-family: "Tinos", "Times New Roman", serif;
  }
  .canvas {
    width: 1200px;
    height: 1189px;
    display: flex;
    flex-direction: column;
    align-items: center;
    justify-content: center;
    gap: 54px;
  }
  .card {
    width: var(--card-w);
    height: var(--card-h);
    background: var(--card);
    border-radius: 26px;
    position: relative;
    box-shadow: 0 10px 28px rgba(0,0,0,.45);
  }

  /* Brand name lockup */
  .brand {
    display: flex;
    align-items: center;
    gap: 16px;
    color: var(--red);
    font-weight: 700;
  }
  .brand-dot {
    width: 34px;
    height: 34px;
    border-radius: 50%;
    background: var(--teal);
    flex: none;
  }
  .brand-name { line-height: 1.05; }

  /* Front */
  .card--front {
    display: flex;
    align-items: center;
    justify-content: center;
  }
  .card--front .brand-name { font-size: 58px; }

  /* Back */
  .card--back {
    display: grid;
    grid-template-columns: 430px 1px 1fr;
    align-items: center;
  }
  .card--back .brand {
    justify-self: center;
    gap: 12px;
  }
  .card--back .brand-dot { width: 26px; height: 26px; }
  .card--back .brand-name { font-size: 36px; width: 300px; }
  .divider {
    height: 200px;
    width: 1px;
    background: var(--teal);
  }
  .contact {
    padding-left: 48px;
    color: var(--teal);
    font-size: 23px;
    line-height: 1.22;
  }
  .contact-name {
    color: var(--red);
    font-weight: 700;
    font-size: 28px;
    letter-spacing: .5px;
    text-transform: uppercase;
  }
  .contact-title { font-size: 22px; margin-bottom: 26px; }
  .contact-address { margin-bottom: 20px; }
  .contact-list { list-style: none; }
  .contact-list li {
    display: flex;
    align-items: center;
    gap: 12px;
    margin-bottom: 6px;
  }
  .icon {
    width: 26px;
    height: 26px;
    border-radius: 4px;
    background: var(--red);
    flex: none;
    display: flex;
    align-items: center;
    justify-content: center;
  }
  .icon svg { width: 16px; height: 16px; fill: none; stroke: var(--card); stroke-width: 2; }
</style>
</head>
<body>
<main class="canvas">

  <section class="card card--front" aria-label="Card front">
    <div class="brand">
      <span class="brand-dot"></span>
      <span class="brand-name">Corvella Language School</span>
    </div>
  </section>

  <section class="card card--back" aria-label="Card back">
    <div class="brand">
      <span class="brand-dot"></span>
      <span class="brand-name">Corvella Language School</span>
    </div>
    <span class="divider"></span>
    <div class="contact">
      <p class="contact-name">Daniel Reyes</p>
      <p class="contact-title">Maneger</p>
      <p class="contact-address">48 Alder Row, 2nd Ste<br>Marlow Heights, Texas 1234</p>
      <ul class="contact-list">
        <li>
          <span class="icon"><svg viewBox="0 0 16 16"><rect x="4" y="1.5" width="8" height="13" rx="1.5"/><line x1="7" y1="12" x2="9" y2="12"/></svg></span>
          555 014 2290
        </li>
        <li>
          <span class="icon"><svg viewBox="0 0 16 16"><path d="M4 2l3 3-1.5 2a8 8 0 0 0 3.5 3.5L11 9l3 3-2 2C7 14 2 9 2 4z"/></svg></span>
          555 014 3318
        </li>
        <li>
          <span class="icon"><svg viewBox="0 0 16 16"><rect x="1.5" y="3.5" width="13" height="9"/><path d="M1.5 3.5l6.5 5 6.5-5"/></svg></span>
          hello@corvellaschool.com
        </li>
      </ul>
    </div>
  </section>

</main>
</body>
</html>
```